Foster/Adoptive Family Ministry needs a postcard design to highlight changed lives

Kin Harbor is a non profit that finds and supports foster and adoptive families for kids in need. We need a postcard design that features families and children who have experienced a changed life by working with Kin Harbor. I'm thinking of a postcard that is custom size...so that it fits in a #10 envelope. So that 3 cards could be printed on an 8 1/2 x 11 card stock. The card should be front and back with a layout for a couple of photos, our logo, a headline and some text that will tell the story of the family. This is all about telling a story. The primary audience for the card is donors, and prospective donors. I don't have photos or the text yet, so I'm looking for an editable layout where I can drop text and photos in.

Industry/Entity Type

Non Profit

```html
<!DOCTYPE html>
<html lang="en">
<head>
<meta charset="utf-8">
<title>Kin Harbor — You Are Changing Lives</title>
<link href="https://fonts.googleapis.com/css2?family=Open+Sans:wght@600;700&family=Pinyon+Script&family=Tinos:ital,wght@0,400;0,700;1,400&family=PT+Sans+Narrow&display=swap" rel="stylesheet">
<style>
  :root{
    --blue-deep:#0f72b9;
    --blue-sky:#2ba7df;
    --navy-script:#2c2a80;
    --ink:#1b1b1b;
    --white:#ffffff;
    --photo-warm:#c9a48a;
    --photo-green:#8fae62;
    --photo-pink:#e7a9b4;
    --photo-autumn:#9b7a4a;
  }
  *{margin:0;padding:0;box-sizing:border-box}
  html,body{width:1200px;height:1047px;overflow:hidden;background:var(--white)}
  .postcard{position:relative;width:1200px;height:1047px}

  /* ---------- front grid ---------- */
  .mosaic{position:absolute;left:0;top:0;width:1200px;height:513px}
  .tile{position:absolute;width:240px;height:128px;display:flex;align-items:center;justify-content:center;
        font-family:"Open Sans",sans-serif;font-weight:600;font-size:28px;color:var(--white);letter-spacing:.2px}
  .tile--deep{background:var(--blue-deep)}
  .tile--sky{background:var(--blue-sky)}
  .tile--tall{height:129px}
  .photo{position:absolute;width:240px;height:128px}
  .photo--family{background:linear-gradient(160deg,#6d9a4c,var(--photo-warm))}
  .photo--mother{background:linear-gradient(120deg,#e9e3df,#d9a184 60%,#eb8c3a)}
  .photo--studio{background:linear-gradient(135deg,var(--photo-pink),#f0dede 60%,#c99786)}
  .photo--walk{background:linear-gradient(160deg,#e2c37c,var(--photo-autumn) 60%,#5a4a33)}
  .photo--hands{background:linear-gradient(120deg,var(--photo-green),#d8b49a 55%,#b8cf7a)}
  .photo--baby{background:linear-gradient(135deg,#f0c9b8,#e8a0a6 60%,#f6d7c9)}
  .photo--embrace{background:linear-gradient(140deg,#5d7c3e,#8a6548 55%,#c99a7c)}

  .headline-panel{position:absolute;left:240px;top:128px;width:720px;height:257px;background:var(--white)}
  .headline{position:absolute;font-family:"Pinyon Script",cursive;color:var(--navy-script);font-weight:400;line-height:1;white-space:nowrap}
  .headline__line1{left:94px;top:50px;font-size:82px}
  .headline__line2{left:166px;top:126px;font-size:82px}

  /* ---------- back ---------- */
  .story{position:absolute;left:0;top:533px;width:852px;height:514px;background:var(--blue-deep);color:var(--white);
         font-family:"Tinos",serif}
  .story__title{position:absolute;left:43px;top:45px;font-size:20px;font-weight:700}
  .story__quote{position:absolute;left:43px;top:102px;width:790px;font-size:33px;font-style:italic;line-height:40px}
  .story__credit{position:absolute;right:33px;top:191px;font-size:21px}
  .story__body{position:absolute;left:43px;width:770px;font-size:22.5px;line-height:28.5px}
  .story__body--one{top:246px}
  .story__body--two{top:330px}

  .brand{position:absolute;left:852px;top:533px;width:348px;height:188px;background:var(--white);
         border:1px solid #9bb9cc;display:flex;align-items:center;justify-content:center}
  .brand__row{display:flex;align-items:center;gap:10px}
  .brand__mark{width:18px;height:18px;border-radius:50%;background:var(--blue-deep)}
  .brand__name{font-family:"Open Sans",sans-serif;font-weight:700;font-size:38px;color:var(--ink);letter-spacing:-.5px}

  .contact{position:absolute;left:852px;top:721px;width:348px;height:326px;background:var(--blue-sky);color:var(--white);
           font-family:"PT Sans Narrow",sans-serif;font-size:25px}
  .contact__label{position:absolute;left:49px;top:40px}
  .contact__address{position:absolute;left:49px;top:85px;line-height:29px;font-style:normal}
  .contact__web{position:absolute;left:49px;top:248px}
</style>
</head>
<body>
<main class="postcard">

  <section class="mosaic">
    <div class="tile tile--deep" style="left:0;top:0">family</div>
    <div class="photo photo--family" style="left:240px;top:0" role="img" aria-label="Photo of a large smiling family with parents and children outdoors"></div>
    <div class="tile tile--sky" style="left:480px;top:0">love</div>
    <div class="photo photo--mother" style="left:720px;top:0" role="img" aria-label="Photo of a mother holding her baby in an orange hat"></div>
    <div class="tile tile--deep" style="left:960px;top:0">fullfillment</div>

    <div class="photo photo--studio" style="left:0;top:128px" role="img" aria-label="Studio photo of a family with young children on a pink backdrop"></div>
    <div class="headline-panel">
      <h1 class="headline headline__line1">You Are</h1>
      <p class="headline headline__line2">Changing Lives</p>
    </div>
    <div class="tile tile--sky tile--tall" style="left:960px;top:128px">joy</div>

    <div class="tile tile--sky" style="left:0;top:256px;height:129px">hope</div>
    <div class="photo photo--walk" style="left:960px;top:257px" role="img" aria-label="Photo of a family walking hand in hand through an autumn forest"></div>

    <div class="photo photo--hands" style="left:0;top:385px" role="img" aria-label="Photo of an adult hand holding a child's hand"></div>
    <div class="photo photo--baby" style="left:240px;top:385px" role="img" aria-label="Photo of a baby girl with a pink flower headband"></div>
    <div class="tile tile--sky" style="left:480px;top:385px">happiness</div>
    <div class="photo photo--embrace" style="left:720px;top:385px" role="img" aria-label="Photo of a mother embracing her young son outdoors"></div>
    <div class="tile tile--deep" style="left:960px;top:385px">enrichment</div>
  </section>

  <section class="story">
    <h2 class="story__title">Why Adopt a Child?</h2>
    <blockquote class="story__quote">“Without my son, I wouldn’t be where I am. I probably wouldn’t even be here today if it wasn’t for adoption.”</blockquote>
    <p class="story__credit">- Dan, adoptive father</p>
    <p class="story__body story__body--one">For that reason, thousands of people every year choose to adopt. And like Dan, without adoption, many of these peoples’ lives would remain unfulfilled.</p>
    <p class="story__body story__body--two">At Kin Harbor we understand that the commitment to adopt is never taken lightly. That's why we're with families from the outset - providing support in making the decision to adopt, immediately after the decision is made, during the actual adoption process and throughout the important support period following your child's arrival home.</p>
  </section>

  <aside class="brand">
    <div class="brand__row">
      <span class="brand__mark"></span>
      <span class="brand__name">Kin Harbor</span>
    </div>
  </aside>

  <aside class="contact">
    <p class="contact__label">For additional information:</p>
    <address class="contact__address">Kin Harbor<br>PO Box 482<br>Cedar Falls, MT&nbsp; 59000<br>406-555-0148</address>
    <p class="contact__web">www.kinharbormontana.org</p>
  </aside>

</main>
</body>
</html>
```